Business Card Design needed for logo design project

This project is linked to Dental Clinic Logo (SEE ATTACHED LOGO FOR GUIDANCE).

Our company needs a Business Card Design. Please refer to our original project in the link above.

Industry/Entity Type

Business

```html
<!DOCTYPE html>
<html lang="en">
<head>
<meta charset="utf-8">
<title>The Ashgrove Dental Clinic – Business Card</title>
<link rel="stylesheet" href="https://fonts.googleapis.com/css2?family=Questrial&family=Open+Sans:wght@300;400&display=swap">
<style>
  :root {
    --page-bg: #e9e9e9;
    --page-bg-edge: #cfcfcf;
    --card-dark: #1b1b1d;
    --card-dark-end: #3a3737;
    --brand-blue: #1c87c9;
    --brand-blue-light: #5b9fd3;
    --box-border: #4aa6e0;
    --text-white: #f4f4f4;
    --text-blue: #3b93d4;
  }
  * { margin: 0; padding: 0; box-sizing: border-box; }
  html, body {
    width: 1200px; height: 1000px; overflow: hidden;
  }
  body {
    background: radial-gradient(ellipse at center, var(--page-bg) 40%, var(--page-bg-edge) 100%);
    position: relative;
  }
  .business-card {
    position: absolute;
    left: 140px; top: 240px;
    width: 920px; height: 520px;
    background: linear-gradient(135deg, var(--card-dark) 0%, var(--card-dark) 45%, var(--card-dark-end) 100%);
    box-shadow: 0 18px 40px rgba(0,0,0,0.35);
    overflow: hidden;
  }
  .brand-mark {
    position: absolute;
    left: 50%; top: 46px;
    transform: translateX(-50%);
    width: 112px; height: 106px;
    background: var(--brand-blue);
    border: 3px solid var(--box-border);
    border-radius: 12px;
  }
  .clinic-name {
    position: absolute;
    left: 0; right: 0; top: 176px;
    text-align: center;
    font-family: "Questrial", sans-serif;
    font-size: 50px;
    letter-spacing: 3px;
    color: var(--text-white);
  }
  .service-list {
    position: absolute;
    top: 268px;
    list-style: none;
    font-family: "Open Sans", sans-serif;
    font-weight: 300;
    font-size: 24px;
    color: var(--text-blue);
  }
  .service-list--left { left: 160px; }
  .service-list--right { left: 520px; top: 262px; }
  .service-list li {
    display: flex; align-items: center;
    height: 37px;
  }
  .tick-box { width: 18px; height: 18px; margin-right: 14px; flex: none; }
  .web-band {
    position: absolute;
    left: 0; right: 0; top: 392px;
    height: 44px;
    background: linear-gradient(90deg, var(--brand-blue) 0%, var(--brand-blue-light) 100%);
    display: flex; align-items: center; justify-content: center;
    font-family: "Open Sans", sans-serif;
    font-size: 22px;
    color: var(--text-white);
  }
</style>
</head>
<body>
  <section class="business-card">
    <div class="brand-mark"></div>
    <h1 class="clinic-name">The Ashgrove Dental Clinic</h1>

    <ul class="service-list service-list--left">
      <li><svg class="tick-box" viewBox="0 0 18 18"><rect width="18" height="18" rx="2" fill="#1c87c9"/><path d="M4 9.5 L7.5 13 L14 5" fill="none" stroke="#fff" stroke-width="2.2"/></svg>Prevention</li>
      <li><svg class="tick-box" viewBox="0 0 18 18"><rect width="18" height="18" rx="2" fill="#1c87c9"/><path d="M4 9.5 L7.5 13 L14 5" fill="none" stroke="#fff" stroke-width="2.2"/></svg>Restoration</li>
      <li><svg class="tick-box" viewBox="0 0 18 18"><rect width="18" height="18" rx="2" fill="#1c87c9"/><path d="M4 9.5 L7.5 13 L14 5" fill="none" stroke="#fff" stroke-width="2.2"/></svg>Dental Implants</li>
    </ul>

    <ul class="service-list service-list--right">
      <li><svg class="tick-box" viewBox="0 0 18 18"><rect width="18" height="18" rx="2" fill="#1c87c9"/><path d="M4 9.5 L7.5 13 L14 5" fill="none" stroke="#fff" stroke-width="2.2"/></svg>Whitening</li>
      <li><svg class="tick-box" viewBox="0 0 18 18"><rect width="18" height="18" rx="2" fill="#1c87c9"/><path d="M4 9.5 L7.5 13 L14 5" fill="none" stroke="#fff" stroke-width="2.2"/></svg>Crown and Veneers</li>
      <li><svg class="tick-box" viewBox="0 0 18 18"><rect width="18" height="18" rx="2" fill="#1c87c9"/><path d="M4 9.5 L7.5 13 L14 5" fill="none" stroke="#fff" stroke-width="2.2"/></svg>Endodontic(root canal)</li>
    </ul>

    <div class="web-band">www.example.com</div>
  </section>
</body>
</html>
```